Website for a Construction Business That Builds Houses

We want some design concepts for this website. Customer likes this competitor site: https://brenwickdwellings.com.au/

We have a logo for Tarvond Constructions. Logo font is Birdman, attached with AI.

Want to be able to change hero images

Will have a contact page.

Need to know what plugins will be used for WordPress.

Coding

Coded - Design and coding required

```html
<!DOCTYPE html>
<html lang="en">
<head>
<meta charset="utf-8">
<title>Tarvond Constructions</title>
<link href="https://fonts.googleapis.com/css2?family=DM+Serif+Text&family=Poppins:wght@400;500;600&display=swap" rel="stylesheet">
<style>
:root{
  --black:#000;
  --ink:#111;
  --white:#fff;
  --grey:#7a7a7a;
  --field:#d9d9d9;
  --line:#d6d6d6;
  --serif:'DM Serif Text', Georgia, serif;
  --sans:'Poppins', Arial, sans-serif;
}
*{margin:0;padding:0;box-sizing:border-box}
html,body{width:1200px;height:2923px;overflow:hidden;background:var(--white);font-family:var(--sans);color:var(--ink)}
.abs{position:absolute}
a{color:inherit;text-decoration:none}

/* header */
.site-header{position:absolute;left:0;top:0;width:1200px;height:88px;background:var(--black);color:var(--white)}
.topbar{position:absolute;left:185px;top:0;width:832px;height:25px;border-bottom:1px solid #555;font-size:9px;display:flex;align-items:center;gap:18px}
.topbar span{display:flex;align-items:center;gap:6px}
.topbar .socials{margin-left:auto;display:flex;gap:5px}
.dot{width:12px;height:12px;border:1px solid var(--white);border-radius:50%}
.brand{position:absolute;left:185px;top:42px;font-size:19px;font-weight:500;display:flex;align-items:center;gap:8px}
.brand i{width:12px;height:12px;border:2px solid var(--white);display:block}
.main-nav{position:absolute;left:452px;top:46px;display:flex;gap:16px;font-size:12px;font-weight:500}
.btn-contact{position:absolute;left:900px;top:40px;width:117px;height:28px;background:var(--white);color:var(--black);font-size:9px;font-weight:600;letter-spacing:1px;display:flex;align-items:center;justify-content:center;gap:5px}

/* hero */
.hero{position:absolute;left:0;top:88px;width:1200px;height:498px;background:linear-gradient(100deg,#e8e6e3 0%,#bdbab5 35%,#8e8d8b 60%,#555 100%)}
.hero-box{position:absolute;left:310px;top:149px;width:472px;height:193px;background:rgba(45,45,45,.88);color:var(--white);text-align:center}
.hero-box h1{font-family:var(--serif);font-weight:400;font-size:32px;line-height:36px;margin-top:26px}
.hero-box p{font-size:10.5px;line-height:15px;text-align:left;margin:26px 40px 0 41px}
.hero-arrows{position:absolute;left:1166px;top:220px}

/* mission */
.eyebrow{font-size:10px;font-weight:600;letter-spacing:1.5px;color:var(--grey);text-transform:uppercase}
.h2{font-family:var(--serif);font-weight:400;font-size:21px;line-height:24px;color:var(--ink)}
.muted{font-size:10.5px;line-height:15px;color:var(--grey)}

.featured-img{position:absolute;left:184px;top:822px;width:509px;height:373px;background:linear-gradient(160deg,#6c6c74 0%,#d9dbe0 45%,#4a3d4d 100%)}
.featured-cap{position:absolute;left:184px;top:1099px;width:509px;height:96px;background:var(--black);color:var(--white)}
.featured-cap h3{font-family:var(--serif);font-weight:400;font-size:17px;position:absolute;left:34px;top:8px}
.featured-cap p{font-size:10px;line-height:15px;position:absolute;left:34px;top:40px;width:330px}
.read-more{font-size:9.5px;font-weight:600;letter-spacing:1px;border-bottom:1px solid currentColor;padding-bottom:3px;display:inline-flex;gap:6px;align-items:center}
.num-card{position:absolute;left:519px;top:967px;width:184px;height:132px;background:var(--white);box-shadow:0 2px 8px rgba(0,0,0,.12);text-align:center}
.num-card b{display:block;font-family:var(--serif);font-weight:400;font-size:54px;margin-top:22px;line-height:60px}
.num-card span{font-size:10.5px;color:var(--grey)}
.stat{position:absolute;top:1104px;width:140px;height:91px;border:1px solid var(--line);text-align:center;font-size:9.5px;color:var(--grey)}
.stat svg{display:block;margin:14px auto 8px}

/* feature rows */
.row{position:absolute;left:0;width:1200px;height:347px;background:var(--black);color:var(--white)}
.row .photo{position:absolute;top:0;height:347px;width:605px;background:linear-gradient(135deg,#2b2b2b 0%,#b7773a 45%,#d8d2c8 60%,#3a3a3a 100%)}
.row .copy{position:absolute;top:91px;width:370px}
.row .eyebrow{color:var(--white)}
.row .h2{color:var(--white);margin-top:14px}
.row p{font-size:10.3px;line-height:15.2px;margin-top:12px}
.row .read-more{margin-top:14px}

/* enquiry */
.enquiry{position:absolute;left:181px;top:2379px;width:842px;height:324px;background:var(--white);box-shadow:0 0 14px rgba(0,0,0,.1)}
.field{position:absolute;background:var(--field);font-size:10.5px;color:#8a8a8a;padding:9px 10px}
.btn-send{position:absolute;left:34px;top:251px;width:150px;height:33px;background:var(--black);color:var(--white);font-size:9.5px;font-weight:600;letter-spacing:1px;display:flex;align-items:center;justify-content:center}
.map{position:absolute;left:542px;top:27px;width:284px;height:274px;background:linear-gradient(180deg,#f2f2f2 0%,#e2e2e2 55%,#9a9a96 100%)}

/* footer */
.site-footer{position:absolute;left:0;top:2628px;width:1200px;height:295px;background:var(--black);color:var(--white)}
.footer-brand{position:absolute;left:185px;top:168px;font-size:20px;font-weight:500;display:flex;align-items:center;gap:8px}
.footer-brand i{width:12px;height:12px;border:2px solid var(--white);display:block}
.footer-col h4{font-family:var(--serif);font-weight:400;font-size:15px;letter-spacing:.5px}
.footer-nav{display:flex;gap:14px;font-size:11px;font-weight:500;margin-top:14px}
.foot-socials{display:flex;gap:8px;margin-top:12px}
.foot-socials .dot{width:17px;height:17px}
</style>
</head>
<body>

<header class="site-header">
  <div class="topbar">
    <span><svg width="10" height="10" viewBox="0 0 24 24" fill="#fff"><path d="M6.6 10.8a15 15 0 0 0 6.6 6.6l2.2-2.2c.3-.3.7-.4 1-.2 1.1.4 2.3.6 3.6.6.6 0 1 .4 1 1V20c0 .6-.4 1-1 1C10.6 21 3 13.4 3 4c0-.6.4-1 1-1h3.5c.6 0 1 .4 1 1 0 1.3.2 2.5.6 3.6.1.3 0 .7-.2 1z"/></svg>(02) 5550 1847</span>
    <span><svg width="10" height="8" viewBox="0 0 24 18" fill="#fff"><path d="M0 0h24v18H0zM2 2l10 7 10-7"/></svg>tarvond@info.com</span>
    <span><svg width="8" height="11" viewBox="0 0 16 22" fill="#fff"><path d="M8 0a8 8 0 0 0-8 8c0 6 8 14 8 14s8-8 8-14a8 8 0 0 0-8-8zm0 11a3 3 0 1 1 0-6 3 3 0 0 1 0 6z"/></svg>48 Larkmoor Lane, New South Wales</span>
    <div class="socials"><i class="dot"></i><i class="dot"></i><i class="dot"></i></div>
  </div>
  <div class="brand"><i></i>Tarvond</div>
  <nav class="main-nav"><a>Home Designs</a><a>Display Homes</a><a>Custom Build</a><a>Knock Down Rebuild</a></nav>
  <a class="btn-contact">CONTACT →</a>
</header>

<section class="hero" role="img" aria-label="Bright open-plan kitchen and living room with marble benchtops and pendant lights">
  <div class="hero-box">
    <h1>Exquisite Designs<br>at Prices You’ll Love</h1>
    <p>Experience the perfect blend of elegance and affordability with our carefully curated spaces designed to meet the highest standards of style and comfort. Whether you're looking to enhance your home or business environment.</p>
  </div>
  <svg class="hero-arrows" width="16" height="60" viewBox="0 0 16 60" fill="none" stroke="#fff" stroke-width="2.5"><path d="M2 10l6-6 6 6M2 44l6 6 6-6"/></svg>
</section>

<section class="mission">
  <div class="abs eyebrow" style="left:185px;top:656px">Our Misssion.</div>
  <h2 class="abs h2" style="left:185px;top:680px">Discover the joy of your dream<br>home with us...</h2>
  <p class="abs muted" style="left:185px;top:744px;width:840px">Experience the perfect blend of elegance and affordability with our carefully curated spaces designed to meet the highest standards of style and comfort. Whether you're looking to enhance your home or business environment.</p>
</section>

<section class="featured">
  <div class="featured-img" role="img" aria-label="Modern white and plum kitchen interior"></div>
  <div class="featured-cap">
    <h3>Featured houseing project</h3>
    <p>Nestled in the heart of Sydney, this exclusive housing project offers a perfect blend of luxury, comfort, and convenience.</p>
    <a class="read-more abs" style="left:393px;top:50px">READ MORE →</a>
  </div>
  <div class="num-card"><b>01</b><span>Featured project</span></div>

  <div class="abs eyebrow" style="left:736px;top:899px">Why Us.</div>
  <h2 class="abs h2" style="left:736px;top:922px">Why Choose Us</h2>
  <p class="abs muted" style="left:736px;top:966px;width:288px">Choosing the right builder is crucial to your home-building journey. At Tarvond, we stand out with our unwavering dedication to excellence, transparency, and customer satisfaction. With years of experience and a reputation for delivering on our promises, we ensure that your experience with us is as smooth and rewarding as possible. Discover why so many trust us to build their dream homes.</p>

  <div class="stat" style="left:734px">
    <svg width="52" height="46" viewBox="0 0 52 46" fill="none" stroke="#222" stroke-width="1.5"><path d="M6 22L24 8l18 14M10 19v22h28V19M18 41V30h8v11M30 28h5v5h-5zM2 41h48"/><circle cx="44" cy="34" r="3"/></svg>
    40 + Projects completed
  </div>
  <div class="stat" style="left:881px">
    <svg width="52" height="46" viewBox="0 0 52 46" fill="none" stroke="#222" stroke-width="1.6"><circle cx="26" cy="14" r="8"/><path d="M12 40c0-8 6-14 14-14s14 6 14 14"/><circle cx="13" cy="18" r="6"/><path d="M2 38c0-6 4-10 9-10"/><circle cx="39" cy="18" r="6"/><path d="M50 38c0-6-4-10-9-10"/></svg>
    45 + Happy Clients
  </div>
</section>

<section class="row" style="top:1300px">
  <div class="copy" style="left:181px">
    <div class="eyebrow">Unveil the beauty</div>
    <h2 class="h2">Unveil the beauty of our<br>exclusive homes.</h2>
    <p>Welcome to a world where every detail is crafted to perfection. Unveil the beauty of our exclusive homes, where luxury meets sophistication and each space is thoughtfully designed to inspire. From the finest materials to the most elegant finishes, our homes are a testament to unparalleled quality and timeless elegance.</p>
    <a class="read-more">READ MORE →</a>
  </div>
  <div class="photo" style="left:595px" role="img" aria-label="Dark kitchen with timber cabinetry and lit splashback"></div>
</section>

<section class="row" style="top:1647px">
  <div class="photo" style="left:0;width:595px" role="img" aria-label="Hallway with timber wall panels and lit floating staircase"></div>
  <div class="copy" style="left:657px">
    <div class="eyebrow">Personalize dream home</div>
    <h2 class="h2">Personalize your dream home with<br>our creative design team.</h2>
    <p>Your dream home is a reflection of your unique style and vision, and we're here to bring it to life. With our creative design team by your side, you have the freedom to personalize every detail, ensuring that your home is truly one-of-a-kind. From selecting the perfect color palettes to customizing floor plans and finishes, our experts work closely with you to turn your ideas into reality.</p>
    <a class="read-more">READ MORE →</a>
  </div>
</section>

<section class="row" style="top:1994px">
  <div class="copy" style="left:181px">
    <div class="eyebrow">Unveil the beauty</div>
    <h2 class="h2">Unveil the beauty of our<br>exclusive homes.</h2>
    <p>Welcome to a world where every detail is crafted to perfection. Unveil the beauty of our exclusive homes, where luxury meets sophistication and each space is thoughtfully designed to inspire. From the finest materials to the most elegant finishes, our homes are a testament to unparalleled quality and timeless elegance.</p>
    <a class="read-more">READ MORE →</a>
  </div>
  <div class="photo" style="left:595px" role="img" aria-label="Dark kitchen with timber cabinetry and lit splashback"></div>
</section>

<footer class="site-footer">
  <div class="footer-brand"><i></i>Tarvond</div>
  <div class="footer-col abs" style="left:332px;top:146px">
    <h4>CONTACT US</h4>
    <p style="font-size:10.5px;line-height:15px;margin-top:12px;width:210px">Our team is dedicated to making your home-building journey as smooth and enjoyable as possible.</p>
  </div>
  <div class="footer-col abs" style="left:627px;top:146px">
    <h4>NAVIGATION</h4>
    <nav class="footer-nav"><a>Home Designs</a><a>Display Homes</a><a>Custom Build</a><a>Knock Down Rebuild</a></nav>
    <div class="foot-socials"><i class="dot"></i><i class="dot"></i><i class="dot"></i></div>
  </div>
</footer>

<section class="enquiry">
  <div class="abs eyebrow" style="left:36px;top:55px">Quick Enquiry.</div>
  <h2 class="abs h2" style="left:36px;top:78px">Want more information?</h2>
  <div class="field" style="left:34px;top:120px;width:249px;height:28px">Your name</div>
  <div class="field" style="left:293px;top:120px;width:226px;height:28px">Your email</div>
  <div class="field" style="left:34px;top:159px;width:485px;height:80px">Message</div>
  <a class="btn-send">SEND MESSAGE →</a>
  <div class="map" role="img" aria-label="Street map showing the office location"></div>
</section>

</body>
</html>
```